Briar Hollow Family Law magazine ad

I need an ad that will run in Tidewell Homes Magazine here in NC. The ad will be a 1/2 page ad, (7.25X4.875). Resolution is 300 dpi or higher.

We are a family law firm (divorce) and we want to high light child custody issues. I would like the ad copy to include our logo (which you can find on our website www.briarhollowfamilylaw.com) and I can send a high res one if you are chosen. Ad MUST include our address and phone number by state law.

Ad copy will be something about protecting children (something brief) like "Protect what you love" or something like that. I will pick quick as I have to turn it in on Wednesday. You will need to be able to email the final product to graphics@tidewellhomesmag.com and me too.

Target Market(s)

Married couples with kids (primarily men) ages 35-50

Industry/Entity Type

Legal

Colors
85cae6
cadf82
fbee3f
fbf289
33a6d7
33b8a4
add136

Requirements
Must have
• website, logo, address, and phone number
Nice to have
• creative and heart provoking (I want the image to make me want to act)
Should not have
• Don't be boring or give me some stock photo I have seen in a million divorce ads.

```html
<!DOCTYPE html>
<html lang="en">
<head>
<meta charset="utf-8">
<title>Briar Hollow Family Law – Half Page Ad</title>
<link rel="stylesheet" href="https://fonts.googleapis.com/css2?family=Montserrat:wght@300;400&display=swap">
<style>
  :root {
    --teal: #00a59b;
    --lime: #b4d46c;
    --white: #ffffff;
    --ink: #3a3a3a;
    --brand-blue: #33a6d7;
    --brand-green: #add136;
  }
  * { box-sizing: border-box; margin: 0; padding: 0; }
  html, body { width: 1200px; height: 807px; overflow: hidden; background: var(--white); }
  body { font-family: "Montserrat", Arial, sans-serif; }

  .ad { position: relative; width: 1200px; height: 807px; background: var(--white); }

  .hero { position: absolute; left: 0; top: 0; width: 1200px; height: 704px; background: var(--teal); }

  .lead {
    position: absolute; right: calc(1200px - 373px); top: 246px;
    text-align: right; color: var(--white);
    font-weight: 300; font-size: 25px; line-height: 27.5px; letter-spacing: 0.2px;
    text-transform: uppercase;
  }
  .divider {
    position: absolute; left: 387px; top: 235px; width: 2px; height: 110px; background: var(--white);
  }
  .headline {
    position: absolute; left: 398px; top: 212px;
    color: var(--lime); font-weight: 300; font-size: 146px; line-height: 1;
    letter-spacing: -2px; white-space: nowrap;
  }
  .cta {
    position: absolute; right: calc(1200px - 946px); top: 357px;
    text-align: right; color: var(--white); font-weight: 300;
  }
  .cta-line { font-size: 20.5px; line-height: 26px; }
  .cta-phone { font-size: 27px; line-height: 36px; margin-top: 4px; }

  .footer { position: absolute; left: 0; top: 704px; width: 1200px; height: 103px; background: var(--white); }
  .brand {
    position: absolute; left: 104px; top: 22px; display: flex; align-items: center; gap: 8px;
  }
  .brand-dot { width: 26px; height: 26px; border-radius: 50%; background: var(--brand-blue); }
  .brand-name {
    font-weight: 400; font-size: 14px; line-height: 16px; color: var(--brand-blue);
    width: 110px;
  }
  .contact {
    position: absolute; left: 245px; top: 18px;
    font-weight: 400; font-size: 11px; line-height: 13.8px; color: var(--ink);
    font-style: normal;
  }
</style>
</head>
<body>
<main class="ad">
  <section class="hero">
    <p class="lead">Your child<br>did not file<br>for divorce.</p>
    <div class="divider"></div>
    <h1 class="headline">YOU DID.</h1>
    <div class="cta">
      <p class="cta-line">Discuss your child’s protection with us.</p>
      <p class="cta-phone">Call 910-555-0182</p>
    </div>
  </section>
  <footer class="footer">
    <div class="brand">
      <span class="brand-dot"></span>
      <span class="brand-name">Briar Hollow Family Law</span>
    </div>
    <address class="contact">
      1420 Larkspur Avenue, Suite 210, Wilmington, NC 28403<br>
      Email: ellen@briarhollowfamilylaw.com<br>
      Phone: 910-555-0182<br>
      Fax: 877-555-0147<br>
      Web: www.briarhollowfamilylaw.com
    </address>
  </footer>
</main>
</body>
</html>
```